KelVor Neutraceuticals Needs a New Label Design!

Kelvor is a neutraceutical line of vitamins, supplements and protein powders. We are looking for a new look/feel for our labels to really make them pop off the shelf.

Some brands we like are:
www.brimu.example
www.velopraxa.example
www.quendil.example

We are going to have square bottles and caps that will most likely be white or clear. We'd like a look/feel that uses bold colors and perhaps foil to make the design stand out.

The labels may be different colors for each product, but the general look/feel should be the same. To learn more about KelVor, take a look at www.tq-pharmlabs.example/kelvor.

We are also reformulating to make our products natural, organic and non-GMO. A look gearing more towards a holistic feel might work!

We have a logo that we cannot change, but we are not committed to the colors of it (Orange and green) and it does NOT have to be prominent on the label itself.

Design must utilize our icons (see website and attached files)

Kelvors tagline is: Shaping Sturdy Lives

Reason: We wanted to extend this project to give designers a bit more time to work on it!

Target Market(s)

Women and Men who are serious about their health, women purchasing vitamins for family....

Industry/Entity Type

Health And Wellness

Font styles to use
Decorative

Requirements
Must have
• Must:
• -Utilize our icons
• -Have bold colors
• -Stand out on a shelf
Nice to have
• The "Vor" in "KelVor" should stand out

```html
<!DOCTYPE html>
<html lang="en">
<head>
<meta charset="utf-8">
<title>Kelvor Mens Multivitamin Label</title>
<link href="https://fonts.googleapis.com/css2?family=Lato:wght@400;700;900&display=swap" rel="stylesheet">
<style>
  :root {
    --page-bg: #eceeef;
    --label-deep: #0b4f9c;
    --label-mid: #1677c8;
    --label-light: #36a5e3;
    --brand-orange: #f2a23a;
    --text-white: #ffffff;
    --text-soft: #d8ecfa;
    --supply-yellow: #ffd45a;
    --tab-navy: #0d3a73;
    --icon-cyan: #5ec3ee;
    --icon-brown: #b88a4c;
    --icon-purple: #7b4bb8;
    --icon-yellow: #f3c623;
    --icon-red: #e23a4a;
    --icon-green: #3aa57b;
  }
  * { margin: 0; padding: 0; box-sizing: border-box; }
  html, body {
    width: 1200px; height: 900px; overflow: hidden;
    background: var(--page-bg);
    font-family: "Lato", sans-serif;
  }
  .label {
    position: absolute; left: 290px; top: 110px;
    width: 620px; height: 680px;
    background:
      radial-gradient(circle at 30% 35%, rgba(120,210,255,0.45), transparent 45%),
      radial-gradient(circle at 80% 75%, rgba(90,190,245,0.35), transparent 40%),
      linear-gradient(180deg, var(--label-deep) 0%, var(--label-mid) 45%, var(--label-light) 75%, var(--label-mid) 100%);
    text-align: center;
    color: var(--text-white);
  }
  .brand-name {
    position: absolute; top: 50px; left: 0; right: 0;
    font-size: 150px; font-weight: 400; line-height: 1;
    color: var(--brand-orange); letter-spacing: -2px;
  }
  .product-line {
    position: absolute; top: 255px; left: 0; right: 0;
    font-size: 62px; font-weight: 900; line-height: 1;
  }
  .product-type {
    position: absolute; top: 325px; left: 0; right: 0;
    font-size: 34px; font-weight: 700; letter-spacing: 6px;
  }
  .product-note {
    position: absolute; top: 372px; left: 90px; right: 90px;
    font-size: 19px; line-height: 1.25; color: var(--text-soft);
  }
  .supply {
    position: absolute; top: 440px; left: 0; right: 0;
    font-size: 42px; font-weight: 700; color: var(--supply-yellow);
  }
  .benefit-icons {
    position: absolute; top: 515px; left: 0; right: 0;
    display: flex; justify-content: center; gap: 14px;
  }
  .benefit-icon {
    width: 60px; height: 60px; border-radius: 10px;
    border: 3px solid rgba(255,255,255,0.85);
  }
  .benefit-icon.brain { background: var(--icon-cyan); }
  .benefit-icon.hair { background: var(--icon-brown); }
  .benefit-icon.digest { background: var(--icon-purple); }
  .benefit-icon.eye { background: var(--icon-yellow); }
  .benefit-icon.heart { background: var(--icon-red); }
  .benefit-icon.joint { background: var(--icon-green); }
  .count-tab {
    position: absolute; bottom: 0; left: 50%; transform: translateX(-50%);
    width: 260px; height: 58px; border-radius: 16px 16px 0 0;
    background: var(--tab-navy);
    font-size: 26px; font-weight: 700; line-height: 58px;
  }
</style>
</head>
<body>
  <section class="label">
    <div class="brand-name">Kelvor</div>
    <div class="product-line">MENS</div>
    <div class="product-type">MULTIVITAMIN</div>
    <p class="product-note">Exclusive Formulation including Signature antioxidants developed for women</p>
    <div class="supply">30 DAY SUPPLY</div>
    <div class="benefit-icons">
      <div class="benefit-icon brain" role="img" aria-label="Brain health icon"></div>
      <div class="benefit-icon hair" role="img" aria-label="Hair and skin health icon"></div>
      <div class="benefit-icon digest" role="img" aria-label="Digestive health icon"></div>
      <div class="benefit-icon eye" role="img" aria-label="Eye health icon"></div>
      <div class="benefit-icon heart" role="img" aria-label="Heart health icon"></div>
      <div class="benefit-icon joint" role="img" aria-label="Joint health icon"></div>
    </div>
    <div class="count-tab">180 CAPSULES</div>
  </section>
</body>
</html>
```